Web Design Project

Design of a complete website that has a quality and professional feel that offers video training. I have uploaded some ideas on how I am visualising the site should operate and hor the pages should interconnect. What I am NOT is a web designer, this is why I am looking for someone with the smarts and vision to make this happen, so I need someone who would like to take on this project and deliver ideas and suggestions to make this work on an automated basis. I am visualising that each page posted should be able to be edited from a back office with images, text, hyperlinks to video views and to document downloads.

Once completed and operational there would be a need for fixes, changes and adjustments as needed though I would envisage basic content would be supplied by me through the back office.

If you dont think that this project can be done within this budget, then please explain to me why and what you believe it is worth to complete. I am happy to consider all options and ideas.
Updates

Project Deadline Extended
Reason: I posted two competitions here on pixel harbor at the same time, logo design and web design. This has delayed my involvement with the web design project as I needed to first settle on a logo design which has now been completed. I have not had a great deal of time available to review submitted designs and of those that have been submitted to date I am not entirely happy with. I will over the next 14 days focus on the web design element. I am wanting a complete website produced and maintained with the design being the first stage. When submitting designs, please provide an indication of if you are interested in going on to produce the complete website and your cost to do this. If you require additional information I can be contacted on kel@brightmarkcoaching.com.au I will be reviewing the submitted designs so far and providing feedback on these and look forward to seeing new ideas. Kel

Target Market(s)

Mostly women with some men, probably a mix of 90/10

Industry/Entity Type

Training

Requirements
Must have
• Fast loading, user friendly, payment option my via quick till account, the site will have a logo (currently being designed on harbor), a customer database that is added to as people take up membership/purchase, needs to have auto reminders of expiring memberships and ability to create e-newsletters with their own hyperlinks to pages and tracking of read items if possible. Back office that can add delete and edit all pages adding links, photos etc.
If you have ideas please express them, I am happy to discuss any issues. I have uploaded an outline of how I am thinking this should be but I am happy to discuss your ideas.

The site needs to operate automatically with subscriptions/memberships payments provision of access to paid for elements

This project needs to be completed in a timely manner.
Nice to have
• ** Auto payment through quick till
** auto registration and access generation
** auto reminders when membership period expires
** Ability to choose what video training is included within the membetship period
** HTML newsletters with tracking
Should not have
• The site should not look unprofessional and unappealing or take a long time to load pages, I am open to colour scheme ideas.

```html
<!DOCTYPE html>
<html lang="en">
<head>
<meta charset="utf-8">
<title>sitename – Video Training</title>
<link href="https://fonts.googleapis.com/css2?family=Arimo:ital,wght@0,400;0,700;1,400;1,700&family=Open+Sans:wght@300;400&family=Roboto+Condensed:wght@400&family=Playfair+Display:ital,wght@0,700;1,900&family=Oswald:wght@400&display=swap" rel="stylesheet">
<style>
:root{
  --pink:#e0627b;
  --pink-dark:#c94a64;
  --pink-soft:#f07290;
  --red:#c8264a;
  --crimson:#d6195a;
  --orange:#ee8a1a;
  --page:#f4eff2;
  --panel:#ffffff;
  --border:#e2dde0;
  --grey-row:#e5e5e5;
  --text:#333333;
  --muted:#555555;
  --date:#a2303c;
  --views:#1d5b8c;
}
*{box-sizing:border-box;margin:0;padding:0}
html,body{width:902px;height:1200px;overflow:hidden}
body{position:relative;background:var(--page);font-family:Arimo,Arial,sans-serif;color:var(--text)}
.abs{position:absolute}

/* header */
.header-band{left:0;top:0;width:902px;height:150px;background:linear-gradient(180deg,#e66f86,#dc5c75);border-bottom:4px solid #f7c9d3}
.header-line{left:0;top:156px;width:902px;height:2px;background:#e8a3b2}
.brand{left:91px;top:24px;font-family:Arimo,Arial,sans-serif;font-weight:700;font-size:36px;color:#fff;letter-spacing:-0.5px}
.sign-in{left:668px;top:21px;font-size:11px;font-weight:700;color:#fff}
.register{left:717px;top:14px;width:98px;height:27px;border-radius:4px;border:1px solid #f7d08a;background:linear-gradient(180deg,#f6a531,#e5761a);color:#fff;font-size:11px;font-weight:700;line-height:25px;text-align:center}
.main-nav{left:402px;top:52px;display:flex;font-family:"Roboto Condensed",sans-serif;font-size:16px;color:#fff}
.main-nav span{padding:3px 11px;height:26px;line-height:20px}
.main-nav .current{background:linear-gradient(180deg,#fafafa,#dcdcdc);color:var(--red);border-radius:3px;margin-right:5px}
.main-nav span+span{margin-left:6px}

/* hero */
.hero{left:82px;top:89px;width:738px;height:337px;border:1px solid #e4e4e4;background:linear-gradient(90deg,#8e8e8e 0%,#bdbdbd 22%,#f2f2f2 42%,#fafafa 70%,#cfcfcf 100%)}
.hero-copy{left:366px;top:155px;text-align:center;width:290px}
.hero-copy .line1{font-family:"Playfair Display",serif;font-weight:700;font-size:21px;color:#222;margin-left:100px}
.hero-copy .line2{font-family:Oswald,sans-serif;font-size:25px;color:#d07a12;line-height:1.1}
.hero-copy .line3{font-family:"Playfair Display",serif;font-style:italic;font-weight:900;font-size:31px;color:#c51a2a;line-height:1.1;white-space:nowrap}
.hero-shadow{left:330px;top:428px;width:240px;height:18px;background:radial-gradient(ellipse at center,rgba(0,0,0,.12),rgba(0,0,0,0) 70%)}

/* sidebar */
.card{background:var(--panel);border:1px solid var(--border);border-radius:5px;box-shadow:0 1px 3px rgba(0,0,0,.06)}
.newsletter{left:80px;top:478px;width:229px;height:109px;padding:13px 13px}
.newsletter p{font-size:10.5px;color:#333}
.newsletter p strong{color:var(--crimson);font-size:13px}
.newsletter .field{margin-top:9px;height:30px;border:1px solid #d4d4d4;border-radius:4px;font-size:9.5px;color:#555;padding:8px 9px}
.newsletter .subscribe{margin-top:8px;width:76px;height:23px;border-radius:3px;background:var(--crimson);color:#fff;font-size:11px;font-weight:700;line-height:23px;text-align:center}
.topics-title{left:80px;top:597px;font-family:"Open Sans",sans-serif;font-weight:400;font-size:19px;color:var(--red)}
.topic-list{left:82px;top:628px;width:225px;list-style:none}
.topic-list li{height:24px;margin-bottom:3px;background:var(--grey-row);border-radius:2px;display:flex;justify-content:space-between;align-items:center;padding:0 9px;font-size:10.5px;color:var(--muted)}
.topic-list li.active{background:var(--pink-soft);color:#fff}
.quote{left:80px;top:909px;width:229px;height:79px;padding:10px 12px 0 26px;font-size:10px;font-style:italic;color:#555;line-height:1.3}
.quote .mark{position:absolute;font-family:"Playfair Display",serif;font-weight:700;font-size:22px;color:var(--red);font-style:normal}
.quote .open{left:8px;top:2px}
.quote .close{right:10px;bottom:-8px}
.quote .by{margin-top:3px;color:var(--red);font-size:9px}

/* featured */
.featured{left:322px;top:478px;width:499px;height:509px}
.featured-bar{left:322px;top:500px;width:499px;height:24px;background:var(--red);color:#fff;font-family:"Open Sans",sans-serif;font-weight:400;font-size:18px;line-height:24px;padding-left:16px}
.video{width:148px}
.thumb{width:148px;height:90px;padding:5px;background:#fff;border:1px solid #ddd;border-radius:4px;box-shadow:0 1px 3px rgba(0,0,0,.12)}
.thumb div{width:100%;height:100%}
.video h3{margin-top:10px;font-size:10px;font-style:italic;font-weight:700;color:var(--red);padding-left:6px}
.video p{margin-top:5px;font-size:10.5px;line-height:1.45;color:#333;padding-left:6px}
.video .meta{margin-top:9px;font-size:9px;color:var(--date);padding-left:6px}
.video .views{margin-top:5px;font-size:9px;color:var(--views);padding-left:6px}
.rule{left:337px;width:469px;border-top:1px dashed #bdbdbd}

/* footer */
.footer-band{left:0;top:1008px;width:902px;height:144px;background:linear-gradient(180deg,#e3667e,#dc5e76)}
.footer-brand{left:44px;top:1062px;width:110px;text-align:center;transform:rotate(-90deg);transform-origin:center;font-family:Arimo,Arial,sans-serif;font-weight:700;font-size:23px;color:#fff}
.footer-nav{left:126px;top:1032px;width:162px;list-style:none;font-family:"Roboto Condensed",sans-serif;font-size:12px;color:#fff}
.footer-nav li{height:25px;line-height:22px;border-bottom:1px solid rgba(255,255,255,.25)}
.footer-nav li:last-child{border-bottom:0}
.explore-title{left:335px;top:1024px;font-size:13px;color:#4a0f1c;text-decoration:underline}
.cat-col{top:1052px;list-style:none;font-size:9.8px;color:#fff;line-height:14.8px;padding-left:6px}
.cat-col.divided{border-left:1px solid rgba(255,255,255,.3);height:88px}
.bottom{left:0;top:1152px;width:902px;height:48px;background:#fff}
.accept{left:84px;top:1167px;font-size:10px;color:#333;display:flex;align-items:center;gap:8px}
.accept .pay{font-size:11px;font-weight:700;color:#1d3d78}
.find{left:330px;top:1167px;font-size:10px;color:#333;display:flex;align-items:center;gap:6px}
.find .net{font-size:9px;color:#2f6aa3}
.copyright{left:594px;top:1168px;font-size:9px;color:var(--red)}
</style>
</head>
<body>

<header>
  <div class="abs header-band"></div>
  <div class="abs header-line"></div>
  <div class="abs brand">sitename</div>
  <div class="abs sign-in">SIGN IN</div>
  <div class="abs register">REGISTER NOW!</div>
  <nav class="abs main-nav">
    <span class="current">HOME</span><span>ABOUT US</span><span>SAMPLE TRAINING VIDEO</span><span>MEMBERSHIPS</span>
  </nav>
</header>

<section>
  <div class="abs hero" role="img" aria-label="Photo of a laptop playing a training video beside a smiling presenter"></div>
  <div class="abs hero-copy">
    <div class="line1">we offer</div>
    <div class="line2">Quality &amp; Professional</div>
    <div class="line3">VIDEO TRAINING</div>
  </div>
  <div class="abs hero-shadow"></div>
</section>

<aside>
  <div class="abs card newsletter">
    <p>Get your newsletter subscription <strong>TODAY</strong></p>
    <div class="field">type your email address here....</div>
    <div class="subscribe">SUBSCRIBE</div>
  </div>
  <h2 class="abs topics-title">Topics</h2>
  <ul class="abs topic-list">
    <li class="active"><span>Accounting</span><span>5</span></li>
    <li><span>Cash Accounting</span><span>12</span></li>
    <li><span>Business</span><span>10</span></li>
    <li><span>Manual Accounting</span><span>2</span></li>
    <li><span>LedgerLite Training Video</span><span>14</span></li>
    <li><span>Accrual Accounting</span><span>17</span></li>
    <li><span>Software Development</span><span>02</span></li>
    <li><span>Payroll</span><span>05</span></li>
    <li><span>BAS Processing</span><span>08</span></li>
    <li><span>Finance</span><span>10</span></li>
  </ul>
  <div class="abs card quote">
    <span class="mark open">“</span>
    With sales reps in 18 countries, getting everyone up to speed was next to impossible. Trainloop makes...
    <div class="by">Marla Quinby, Kestrel Health</div>
    <span class="mark close">”</span>
  </div>
</aside>

<main>
  <div class="abs card featured"></div>
  <h2 class="abs featured-bar">Featured Videos</h2>

  <article class="abs video" style="left:336px;top:538px">
    <div class="thumb"><div role="img" aria-label="Screen recording of a software tutorial" style="background:linear-gradient(135deg,#1d5fa8,#4aa2d8 60%,#123c6e)"></div></div>
    <h3>Lorem ipsum dolor</h3>
    <p>Eusmod tempor incididunt labore et dolore magna aliqua Ut enim ad minim...</p>
    <div class="meta">Date: 01/09Length: 03:35</div>
    <div class="views">Views: 177243</div>
  </article>
  <article class="abs video" style="left:497px;top:538px">
    <div class="thumb"><div role="img" aria-label="Screen recording of a spreadsheet lesson" style="background:linear-gradient(160deg,#222 40%,#7a2a10 75%,#111)"></div></div>
    <h3>Lorem ipsum dolor</h3>
    <p>Eusmod tempor incididunt labore et dolore magna aliqua Ut enim ad minim...</p>
    <div class="meta">Date: 01/09Length: 03:35</div>
    <div class="views">Views: 177243</div>
  </article>
  <article class="abs video" style="left:658px;top:538px">
    <div class="thumb"><div role="img" aria-label="Recording of a conference keynote" style="background:linear-gradient(180deg,#1a2a5a,#3d5aa0 55%,#0d1633)"></div></div>
    <h3>Lorem ipsum dolor</h3>
    <p>Eusmod tempor incididunt labore et dolore magna aliqua Ut enim ad minim...</p>
    <div class="meta">Date: 01/09Length: 03:35</div>
    <div class="views">Views: 177243</div>
  </article>

  <div class="abs rule" style="top:750px"></div>

  <article class="abs video" style="left:336px;top:769px">
    <div class="thumb"><div role="img" aria-label="Screen recording of a software tutorial" style="background:linear-gradient(135deg,#2b6d6a,#7ec3b6 60%,#1f4d4a)"></div></div>
    <h3>Lorem ipsum dolor</h3>
    <p>Eusmod tempor incididunt labore et dolore magna aliqua Ut enim ad minim...</p>
    <div class="meta">Date: 01/09Length: 03:35</div>
    <div class="views">Views: 177243</div>
  </article>
  <article class="abs video" style="left:497px;top:769px">
    <div class="thumb"><div role="img" aria-label="Screen recording of a spreadsheet lesson" style="background:linear-gradient(160deg,#2a0a12 35%,#b3203e 75%,#1a0509)"></div></div>
    <h3>Lorem ipsum dolor</h3>
    <p>Eusmod tempor incididunt labore et dolore magna aliqua Ut enim ad minim...</p>
    <div class="meta">Date: 01/09Length: 03:35</div>
    <div class="views">Views: 177243</div>
  </article>
  <article class="abs video" style="left:658px;top:769px">
    <div class="thumb"><div role="img" aria-label="Recording of a conference keynote" style="background:linear-gradient(180deg,#3a3518,#9a8c45 55%,#221f0c)"></div></div>
    <h3>Lorem ipsum dolor</h3>
    <p>Eusmod tempor incididunt labore et dolore magna aliqua Ut enim ad minim...</p>
    <div class="meta">Date: 01/09Length: 03:35</div>
    <div class="views">Views: 177243</div>
  </article>
</main>

<footer>
  <div class="abs footer-band"></div>
  <div class="abs footer-brand">sitename</div>
  <ul class="abs footer-nav">
    <li>HOME</li><li>ABOUT US</li><li>SAMPLE TRAINING VIDEO</li><li>MEMBERSHIPS</li>
  </ul>
  <h3 class="abs explore-title">Explore Categories</h3>
  <ul class="abs cat-col" style="left:329px">
    <li>Cars and Other Vehicles</li><li>Computers and Electronics</li><li>Education and Communications</li><li>Family Life</li><li>Finance and Business</li>
  </ul>
  <ul class="abs cat-col divided" style="left:537px">
    <li>Food and Entertaining</li><li>Health</li><li>Hobbies and Crafts</li><li>Holidays and Traditions</li><li>Home and Garden</li>
  </ul>
  <ul class="abs cat-col divided" style="left:701px">
    <li>Other</li><li>Personal Care and Style</li><li>Pets and Animals</li><li>Philosophy and Religion</li><li>Relationships</li><li>Sports and Fitness Travel</li>
  </ul>

  <div class="abs bottom"></div>
  <div class="abs accept">We accept: <span class="pay">quick till</span><span class="pay">Cardwise</span><span class="pay">Tallycard</span></div>
  <div class="abs find">Find us on: <span class="net">Murmur</span><span class="net">Circlet</span><span class="net">Reelhub</span><span class="net">Pinwell</span><span class="net">Feedline</span></div>
  <div class="abs copyright">Copyright©2012 www.sitename.com &nbsp; All rights reserved</div>
</footer>

</body>
</html>
```